Forest Consultant/Timber Buyer needs a clean business card

We are a forestry consulting and timber buying company. We meet with private landowners and assist them with timber management and timber harvesting. We would like a professional business card, please no clip art. logo is blue and white but would like to see a gray,silver, or some other color incorporated. Would like basic contact info. Would like to the layout to be creative and sleek but masculine.

Target Market(s)

private landowners

Industry/Entity Type

Business

Contact Information for Business Card

name,position, cell number, office number, email, website. This might be to cluttered. Basic contact info is what we are looking for.

Contact info can all be on one side with logo on the other.

Font styles to use
Serif
Sans Serif

Colors
0255a3
ffffff
aaaaaa

Requirements
Must have
• We just want it professional.
Nice to have
• Creative layout.
Should not have
• please no clip art of log trucks etc.

```html
<!DOCTYPE html>
<html lang="en">
<head>
<meta charset="utf-8">
<title>Ridgeline Forestry – Business Card</title>
<link rel="stylesheet" href="https://fonts.googleapis.com/css2?family=EB+Garamond:wght@400;600&display=swap">
<style>
  :root {
    --brand-blue: #0255a3;
    --deep-blue: #0a4a8a;
    --paper: #ffffff;
    --paper-shade: #eef1f4;
    --silver: #aaaaaa;
    --ink-light: #d4dde8;
    --stage: #e4e6e9;
  }
  * { box-sizing: border-box; margin: 0; padding: 0; }
  html, body {
    width: 1200px; height: 873px; overflow: hidden;
    background: var(--stage);
    font-family: "EB Garamond", Georgia, serif;
  }
  .canvas {
    width: 1200px; height: 873px;
    display: flex; flex-direction: column;
    align-items: center; justify-content: center; gap: 44px;
  }
  .card {
    position: relative;
    width: 560px; height: 320px;
    background: var(--paper);
    overflow: hidden;
    box-shadow: 0 6px 18px rgba(0,0,0,.18);
  }

  /* Company name */
  .brand {
    position: absolute;
    display: flex; align-items: center; gap: 14px;
    color: var(--brand-blue);
    font-size: 40px; font-weight: 600; line-height: 1;
    white-space: nowrap;
  }
  .brand-square {
    width: 22px; height: 22px;
    background: var(--brand-blue);
    flex: none;
  }

  /* Name side */
  .card--logo {
    background: linear-gradient(160deg, var(--paper) 0%, var(--paper-shade) 100%);
  }
  .card--logo .brand { left: 0; right: 0; top: 138px; justify-content: center; }

  /* Contact side */
  .card--contact .brand { left: 78px; top: 70px; }
  .rule {
    position: absolute; left: 0; right: 0; height: 2px;
    background: var(--brand-blue);
  }
  .rule--one { top: 176px; }
  .rule--two { top: 183px; }
  .contact-band {
    position: absolute; left: 0; right: 0; top: 192px; bottom: 0;
    background: var(--deep-blue);
    color: var(--ink-light);
  }
  .contact-list {
    position: absolute; left: 40px; top: 36px;
    list-style: none; font-size: 15px; line-height: 26px;
  }
  .contact-list li { display: flex; align-items: center; gap: 12px; }
  .contact-list svg { width: 15px; height: 15px; fill: var(--ink-light); }
  .divider {
    position: absolute; left: 300px; top: 0; bottom: 22px;
    width: 1px; background: var(--ink-light); opacity: .8;
  }
  .person {
    position: absolute; left: 326px; top: 10px;
    font-size: 14px; line-height: 18px;
  }
  .person-name { font-size: 18px; font-weight: 600; color: #c9d2dc; }
  .person-title { color: var(--silver); margin-bottom: 14px; }
  .person-address { font-style: normal; }
</style>
</head>
<body>
<main class="canvas">

  <section class="card card--logo" aria-label="Business card, company side">
    <div class="brand">
      <span class="brand-square"></span>
      <span class="brand-name">Ridgeline Forestry</span>
    </div>
  </section>

  <section class="card card--contact" aria-label="Business card, contact side">
    <div class="brand">
      <span class="brand-square"></span>
      <span class="brand-name">Ridgeline Forestry</span>
    </div>
    <div class="rule rule--one"></div>
    <div class="rule rule--two"></div>
    <div class="contact-band">
      <ul class="contact-list">
        <li>
          <svg viewBox="0 0 16 16" aria-hidden="true"><path d="M2 5c0-2 2-3 6-3s6 1 6 3v1h-3V5H5v1H2zM4 7h8l2 6H2z"/></svg>
          412-555-0120
        </li>
        <li>
          <svg viewBox="0 0 16 16" aria-hidden="true"><path d="M4 1h8v4H4zM1 6h14v6h-3v3H4v-3H1zM5 10v4h6v-4z"/></svg>
          412-555-0122
        </li>
        <li>
          <svg viewBox="0 0 16 16" aria-hidden="true"><path d="M1 3h14v10H1zM2.5 4.5 8 9l5.5-4.5v-.2h-11z"/></svg>
          dan@hartwellforestry.com
        </li>
      </ul>
      <div class="divider"></div>
      <div class="person">
        <p class="person-name">Daniel Hartwell</p>
        <p class="person-title">Chief Operating Officer</p>
        <address class="person-address">48 Cedar Hollow Road,<br>Millbrook, PA 15010</address>
      </div>
    </div>
  </section>

</main>
</body>
</html>
```